RW Frameworks Inc Business cards

We need business cards using our existing logo but slightly modified. Right now the logo says RW Framework Masonry. We want to keep the RW part of the design, but replace the Framework Masonry portion with "FRAMEWORKS". Please see the attached file.
Ideally this would be a blank template so we can add Different Names, titles, and phone numbers later.
On the one side we want only the logo and on the other side the detail. I'm attaching an example for you to see.
Please reach out with any other questions. Our address and other details will be given out once we find a design we like.

Target Market(s)

Construction Industry

```html
<!DOCTYPE html>
<html lang="en">
<head>
<meta charset="utf-8">
<title>RW Frameworks Inc – Business Cards</title>
<link rel="stylesheet" href="https://fonts.googleapis.com/css2?family=Lexend:wght@300;400;600&display=swap">
<style>
  :root {
    --backdrop: #e3e4e6;
    --brand-blue: #0a72c4;
    --brand-blue-deep: #0668b4;
    --card-white: #f0f0f1;
    --rim-grey: #808286;
    --text-light: #ffffff;
  }
  * { margin: 0; padding: 0; box-sizing: border-box; }
  html, body {
    width: 1200px;
    height: 900px;
    overflow: hidden;
    background: var(--backdrop);
    font-family: "Lexend", sans-serif;
  }
  .sheet {
    width: 1200px;
    height: 900px;
    display: flex;
    flex-direction: column;
    align-items: center;
    justify-content: center;
    gap: 36px;
  }
  .card {
    position: relative;
    width: 700px;
    height: 400px;
    overflow: hidden;
    box-shadow: 0 6px 18px rgba(0,0,0,0.18);
  }
  .card-art { position: absolute; inset: 0; }

  /* Detail side */
  .holder { position: absolute; left: 49px; top: 62px; color: var(--text-light); }
  .holder-name { font-weight: 600; font-size: 26px; letter-spacing: -0.3px; line-height: 1; }
  .holder-title { font-weight: 300; font-size: 16px; margin-top: 10px; }
  .divider {
    position: absolute; left: 49px; top: 213px;
    width: 18px; height: 2px; background: var(--text-light);
  }
  .address {
    position: absolute; left: 49px; top: 234px;
    color: var(--text-light); font-weight: 300; font-size: 15.5px; line-height: 20px;
  }
  .contacts {
    position: absolute; left: 49px; top: 290px;
    list-style: none; color: var(--text-light); font-weight: 300; font-size: 15.5px;
  }
  .contacts li { display: flex; align-items: center; gap: 10px; height: 26px; }
  .contacts svg { width: 16px; height: 16px; flex: none; }

  .wordmark {
    position: absolute;
    text-align: center;
    font-weight: 600;
    line-height: 1;
  }
  .wordmark-front {
    left: 410px; width: 270px; top: 150px;
    color: var(--brand-blue);
  }
  .wordmark-back {
    left: 0; width: 700px; top: 130px;
    color: var(--text-light);
  }
  .wordmark .mark-initials { display: block; font-size: 78px; letter-spacing: 2px; }
  .wordmark .mark-name { display: block; font-size: 18px; letter-spacing: 9px; margin-top: 14px; padding-left: 9px; }
  .wordmark-back .mark-initials { font-size: 92px; }
  .wordmark-back .mark-name { font-size: 22px; letter-spacing: 12px; padding-left: 12px; }
</style>
</head>
<body>
<main class="sheet">

  <section class="card card-detail" aria-label="Business card, detail side">
    <svg class="card-art" viewBox="0 0 700 400" aria-hidden="true">
      <defs>
        <linearGradient id="blueField" x1="0" y1="0" x2="1" y2="1">
          <stop offset="0" stop-color="var(--brand-blue-deep)"/>
          <stop offset="1" stop-color="var(--brand-blue)"/>
        </linearGradient>
      </defs>
      <rect width="700" height="400" fill="url(#blueField)"/>
      <circle cx="576" cy="200" r="206" fill="var(--rim-grey)"/>
      <circle cx="582" cy="200" r="206" fill="var(--card-white)"/>
      <rect x="640" y="0" width="60" height="400" fill="var(--card-white)"/>
      <rect x="-8" y="68" width="30" height="44" rx="7" fill="var(--card-white)"/>
    </svg>

    <div class="holder">
      <div class="holder-name">DANA MORLEY</div>
      <div class="holder-title">FOUNDER</div>
    </div>
    <div class="divider"></div>
    <p class="address">YOUR LOCATION STREET<br>HERE UNITED STREET-9100</p>
    <ul class="contacts">
      <li>
        <svg viewBox="0 0 16 16" aria-hidden="true"><path d="M3.5 1.5l2.3 2.8-1.3 1.6c.9 2 2.5 3.6 4.6 4.6l1.6-1.3 2.8 2.3-1.6 2.3C6.8 13.5 2.5 9.2 1.3 3.1z" fill="none" stroke="#fff" stroke-width="1.2" stroke-linejoin="round"/><path d="M9.5 2.5a4 4 0 0 1 4 4M9.5 4.8a1.8 1.8 0 0 1 1.8 1.8" fill="none" stroke="#fff" stroke-width="1.1"/></svg>
        +000000000000
      </li>
      <li>
        <svg viewBox="0 0 16 16" aria-hidden="true"><rect x="1" y="3.5" width="14" height="9.5" fill="none" stroke="#fff" stroke-width="1.2"/><path d="M1 3.5l7 5.5 7-5.5M1 13l5.2-5M15 13l-5.2-5" fill="none" stroke="#fff" stroke-width="1.2"/></svg>
        INFO@YOURMAIL.COM
      </li>
      <li>
        <svg viewBox="0 0 16 16" aria-hidden="true"><circle cx="8" cy="8" r="6.6" fill="none" stroke="#fff" stroke-width="1.2"/><path d="M2 6.5h12M2 9.5h12M8 1.4c-3 3.5-3 9.7 0 13.2M8 1.4c3 3.5 3 9.7 0 13.2" fill="none" stroke="#fff" stroke-width="1"/></svg>
        WWW.YOURWEBSITE.COM
      </li>
    </ul>

    <div class="wordmark wordmark-front">
      <span class="mark-initials">RW</span>
      <span class="mark-name">FRAMEWORKS</span>
    </div>
  </section>

  <section class="card card-logo" aria-label="Business card, logo side">
    <svg class="card-art" viewBox="0 0 700 400" aria-hidden="true">
      <rect width="700" height="400" fill="var(--brand-blue)"/>
    </svg>
    <div class="wordmark wordmark-back">
      <span class="mark-initials">RW</span>
      <span class="mark-name">FRAMEWORKS</span>
    </div>
  </section>

</main>
</body>
</html>
```